Organic lawn care

take the same sign as the mosquito sign, only instead of the mosquito image have the red circle and line cross out the text of "chemicals". Have the sign say "this lawn receives ORGANIC grass treatments" "instantly SAFE for people and pets"

Lawn Care

```html
<!DOCTYPE html>
<html lang="en">
<head>
<meta charset="utf-8">
<title>Organic Lawn Care Signs</title>
<link href="https://fonts.googleapis.com/css2?family=Anton&family=Arimo:wght@700&display=swap" rel="stylesheet">
<style>
  :root {
    --sign-yellow: #ffec00;
    --sign-white: #ffffff;
    --ink-dark: #2e2e2e;
    --ink-black: #111111;
    --accent-red: #e3201f;
    --panel-edge: #c9c9c9;
    --page-bg: #ffffff;
  }
  * { box-sizing: border-box; margin: 0; padding: 0; }
  html, body {
    width: 818px;
    height: 1200px;
    overflow: hidden;
    background: var(--page-bg);
  }
  .sign-sheet {
    width: 818px;
    height: 1200px;
    padding: 4px;
    display: grid;
    grid-template-columns: 1fr 1fr;
    grid-template-rows: 1fr 1fr;
    gap: 6px;
  }
  .sign {
    position: relative;
    border: 2px solid var(--panel-edge);
    display: flex;
    flex-direction: column;
    align-items: center;
    text-align: center;
    color: var(--ink-dark);
    --headline: var(--ink-dark);
  }
  .sign--yellow { background: var(--sign-yellow); }
  .sign--white { background: var(--sign-white); }
  .sign--red-type { --headline: var(--accent-red); }

  .sign__intro {
    margin-top: 18px;
    font-family: "Arimo", Arial, sans-serif;
    font-weight: 700;
    font-size: 25px;
    line-height: 1;
    color: var(--ink-dark);
  }
  .sign__headline {
    margin-top: 4px;
    font-family: "Anton", Impact, sans-serif;
    font-size: 46px;
    line-height: 1.0;
    letter-spacing: 0.5px;
    color: var(--headline);
  }
  .no-chemicals {
    position: relative;
    width: 260px;
    height: 260px;
    margin-top: 18px;
  }
  .no-chemicals svg {
    position: absolute;
    inset: 0;
  }
  .no-chemicals__word {
    position: absolute;
    left: 50%;
    top: 50%;
    transform: translate(-50%, -50%) scaleY(1.15);
    font-family: "Anton", Impact, sans-serif;
    font-size: 66px;
    line-height: 1;
    color: var(--ink-black);
    white-space: nowrap;
  }
  .sign__safe {
    margin-top: 22px;
    font-family: "Anton", Impact, sans-serif;
    font-size: 50px;
    line-height: 1;
    letter-spacing: 0.5px;
    color: var(--headline);
  }
  .sign__audience {
    margin-top: 8px;
    font-family: "Arimo", Arial, sans-serif;
    font-weight: 700;
    font-size: 29px;
    line-height: 1;
    color: var(--headline);
  }
</style>
</head>
<body>
<main class="sign-sheet">

  <section class="sign sign--yellow">
    <p class="sign__intro">this lawn receives</p>
    <h2 class="sign__headline">ORGANIC GRASS<br>TREATMENTS</h2>
    <div class="no-chemicals">
      <svg viewBox="0 0 260 260" aria-hidden="true">
        <circle cx="130" cy="130" r="114" fill="none" stroke="#e3201f" stroke-width="22"/>
        <line x1="50" y1="50" x2="210" y2="210" stroke="#e3201f" stroke-width="22"/>
      </svg>
      <span class="no-chemicals__word">CHEMICALS</span>
    </div>
    <p class="sign__safe">INSTANTLY SAFE</p>
    <p class="sign__audience">for people and pets</p>
  </section>

  <section class="sign sign--white">
    <p class="sign__intro">this lawn receives</p>
    <h2 class="sign__headline">ORGANIC GRASS<br>TREATMENTS</h2>
    <div class="no-chemicals">
      <svg viewBox="0 0 260 260" aria-hidden="true">
        <circle cx="130" cy="130" r="114" fill="none" stroke="#e3201f" stroke-width="22"/>
        <line x1="50" y1="50" x2="210" y2="210" stroke="#e3201f" stroke-width="22"/>
      </svg>
      <span class="no-chemicals__word">CHEMICALS</span>
    </div>
    <p class="sign__safe">INSTANTLY SAFE</p>
    <p class="sign__audience">for people and pets</p>
  </section>

  <section class="sign sign--yellow sign--red-type">
    <p class="sign__intro">this lawn receives</p>
    <h2 class="sign__headline">ORGANIC GRASS<br>TREATMENTS</h2>
    <div class="no-chemicals">
      <svg viewBox="0 0 260 260" aria-hidden="true">
        <circle cx="130" cy="130" r="114" fill="none" stroke="#e3201f" stroke-width="22"/>
        <line x1="50" y1="50" x2="210" y2="210" stroke="#e3201f" stroke-width="22"/>
      </svg>
      <span class="no-chemicals__word">CHEMICALS</span>
    </div>
    <p class="sign__safe">INSTANTLY SAFE</p>
    <p class="sign__audience">for people and pets</p>
  </section>

  <section class="sign sign--white sign--red-type">
    <p class="sign__intro">this lawn receives</p>
    <h2 class="sign__headline">ORGANIC GRASS<br>TREATMENTS</h2>
    <div class="no-chemicals">
      <svg viewBox="0 0 260 260" aria-hidden="true">
        <circle cx="130" cy="130" r="114" fill="none" stroke="#e3201f" stroke-width="22"/>
        <line x1="50" y1="50" x2="210" y2="210" stroke="#e3201f" stroke-width="22"/>
      </svg>
      <span class="no-chemicals__word">CHEMICALS</span>
    </div>
    <p class="sign__safe">INSTANTLY SAFE</p>
    <p class="sign__audience">for people and pets</p>
  </section>

</main>
</body>
</html>
```